hop3PeakTrail

I have a weebly web site need design and formatted using the color and look and feel similar to another site. Our web site is currently behind password. http://www.hop3peaktrail.com pwd Blue7RiverLamp!

I'm looking to layout like https://www.kravlinpartners.com/blog

We want a yellow, light yellow, gray and black as the main colors. Attached image show color of yellow and light yellow. I don't have a specific color for gray and black. If you think there should be addition colors in the color pallet we greatly appreciate your expertise.

We need the logo designed. Right now its just text.

I don't like that our site list the full blog one after another, I like the tiled look, image, tile and small amount of text. Click and go into a blog. Often at the end of a blog you can jump back to main page, and/or see three additional blog tiles. We like how orange carries through on buttons and text, Accent colors are consistent.

I need CSS that can be inserted into each form. If you look at the source of the form, you can see how I tried to format given the form elements. I cannot change the form, but I can easily insert CSS for the form.

I need a template that can be used in Weebly site either you edit on our site or give us a template that can be used.

Industry/Entity Type

Life Coaching

Coding

Coded - Design and coding required

Number of Pages Required

5+ page

Font styles to use
Sans Serif

Requirements
Must have
• What to build a clean color pallet using the Yellow, light yellow I uploaded image. Also a gray and black.

```html
<!DOCTYPE html>
<html lang="en">
<head>
<meta charset="utf-8">
<title>hop3PeakTrail – Pricing</title>
<link href="https://fonts.googleapis.com/css2?family=IBM+Plex+Sans:wght@400;500;600&family=Oswald:wght@500;600&family=Roboto:wght@500;700&family=Montserrat:wght@600&display=swap" rel="stylesheet">
<style>
:root{
  --yellow:#fdbf00;
  --ink:#111111;
  --text:#333333;
  --muted:#9aa0b4;
  --line:#ececec;
  --footer:#151515;
  --white:#ffffff;
}
*{box-sizing:border-box;margin:0;padding:0}
html,body{width:1030px;height:1200px;overflow:hidden;background:var(--white)}
body{position:relative;font-family:"IBM Plex Sans",sans-serif;color:var(--text)}
.site-header{position:absolute;top:0;left:0;width:1030px;height:61px;background:var(--white)}
.brand{position:absolute;left:85px;top:12px;font-family:"IBM Plex Sans",sans-serif;font-weight:600;font-size:28px;color:var(--ink);letter-spacing:-.3px}
.main-nav{position:absolute;top:23px;font-family:"Roboto",sans-serif;font-weight:700;font-size:11.5px;color:var(--ink)}
.main-nav span{position:absolute;white-space:nowrap}
.btn-subscribe{position:absolute;left:806px;top:13px;width:138px;height:34px;background:var(--yellow);font-family:"Roboto",sans-serif;font-weight:700;font-size:12px;color:var(--ink);display:flex;align-items:center;justify-content:center}
.hero{position:absolute;top:61px;left:0;width:1030px;height:241px;background:linear-gradient(180deg,#5a6f9c 0%,#9a7d9c 35%,#e39a6e 70%,#f6c87a 100%)}
.hero-title{position:absolute;left:85px;top:105px;font-family:"Oswald",sans-serif;font-weight:600;font-size:50px;color:var(--white);letter-spacing:.5px}
.intro{position:absolute;left:90px;top:347px;width:850px;text-align:center;font-size:15px;line-height:23px;color:var(--text)}
.plan{position:absolute;top:489px;width:211px;height:322px;border:1px solid var(--line);background:var(--white);padding:20px 21px}
.plan.featured{background:var(--yellow);border-color:var(--yellow);box-shadow:0 4px 14px rgba(0,0,0,.08);padding-top:17px}
.plan-name{display:inline-block;font-weight:600;font-size:12.5px;color:var(--ink);padding-bottom:2px;border-bottom:2px solid var(--yellow)}
.featured .plan-name{border-color:var(--ink)}
.plan-price{font-family:"Oswald",sans-serif;font-weight:500;font-size:27px;color:var(--ink);margin-top:4px;line-height:40px}
.features{list-style:none;margin-top:6px}
.features li{position:relative;padding-left:13px;font-size:11.2px;line-height:16px;margin-bottom:7px;color:var(--text)}
.featured .features li{color:var(--ink)}
.features svg{position:absolute;left:0;top:4px;width:8px;height:8px}
.btn-plan{position:absolute;left:21px;top:266px;width:137px;height:34px;border:1.5px solid var(--ink);font-family:"Roboto",sans-serif;font-weight:700;font-size:12px;color:var(--ink);display:flex;align-items:center;justify-content:center}
.featured .btn-plan{background:var(--ink);color:var(--white)}
.site-footer{position:absolute;top:894px;left:0;width:1030px;height:306px;background:var(--footer);color:var(--white)}
.footer-brand{position:absolute;left:84px;top:92px;font-weight:600;font-size:30px}
.footer-head{position:absolute;top:92px;font-family:"Montserrat",sans-serif;font-weight:600;font-size:14.5px}
.footer-menu{position:absolute;left:335px;top:120px;list-style:none;font-size:13px}
.footer-menu li{line-height:27px}
.email-field{position:absolute;left:531px;top:124px;width:205px;height:36px;border:1px solid #d8d8d8;font-size:10.5px;padding:11px 10px;color:#e0e0e0}
.btn-submit{position:absolute;left:532px;top:167px;width:99px;height:34px;background:var(--yellow);color:var(--ink);font-family:"Roboto",sans-serif;font-weight:500;font-size:13px;display:flex;align-items:center;justify-content:center}
.social{position:absolute;left:800px;top:125px}
.footer-rule{position:absolute;left:83px;top:246px;width:859px;border-top:1px solid #333}
.copyright{position:absolute;left:0;width:1030px;top:262px;text-align:center;font-size:13px}
</style>
</head>
<body>
<header class="site-header">
  <div class="brand">hop3PeakTrail</div>
  <nav class="main-nav">
    <span style="left:352px">WHO WE ARE</span>
    <span style="left:457px">OUR MODEL</span>
    <span style="left:557px">WHO USES HOP3PEAKTRAIL</span>
    <span style="left:732px">PRICING</span>
  </nav>
  <div class="btn-subscribe">SUBSCRIBE NOW</div>
</header>

<section class="hero" role="img" aria-label="Person in a hooded top raising both arms toward a sunset sky">
  <h1 class="hero-title">PRICING</h1>
</section>

<p class="intro">Getting the right amount of coaching or guidance can be tricky. Some people choose t do it on their own, while others want to go all in and learn everything they can from a coach. At hop3PeakTrail we offer as much help as needed. So whether you are a "Do It Yourself" (DIY) or a person who wants someone that knows you and can give the best advice across your life, we have a plan that is right for you.</p>

<svg width="0" height="0" style="position:absolute">
  <defs>
    <symbol id="tick-muted" viewBox="0 0 10 10"><circle cx="5" cy="5" r="5" fill="#9aa0b4"/><path d="M2.8 5.2l1.6 1.5 2.9-3" stroke="#fff" stroke-width="1.3" fill="none"/></symbol>
    <symbol id="tick-dark" viewBox="0 0 10 10"><circle cx="5" cy="5" r="5" fill="#111"/><path d="M2.8 5.2l1.6 1.5 2.9-3" stroke="#fdbf00" stroke-width="1.3" fill="none"/></symbol>
  </defs>
</svg>

<article class="plan" style="left:75px">
  <div class="plan-name">DIY</div>
  <div class="plan-price">Free</div>
  <ul class="features">
    <li><svg><use href="#tick-muted"/></svg>Personal Check Up Questionnaire</li>
    <li><svg><use href="#tick-muted"/></svg>E-Mail Questions</li>
    <li><svg><use href="#tick-muted"/></svg>Use of Coaching Tools</li>
  </ul>
  <div class="btn-plan">CHOOSE PLAN</div>
</article>

<article class="plan" style="left:298px">
  <div class="plan-name">Bronze</div>
  <div class="plan-price">$9.95</div>
  <ul class="features">
    <li><svg><use href="#tick-muted"/></svg>Personal Check Up Questionnaire</li>
    <li><svg><use href="#tick-muted"/></svg>E-Mail Questions</li>
    <li><svg><use href="#tick-muted"/></svg>Use of Coaching Tools</li>
    <li><svg><use href="#tick-muted"/></svg>SMS Communication</li>
    <li style="line-height:23px"><svg><use href="#tick-muted"/></svg>Online 30 Minute Call/Meeting - One per Quarter</li>
  </ul>
  <div class="btn-plan">CHOOSE PLAN</div>
</article>

<article class="plan featured" style="left:521px">
  <div class="plan-name">Silver</div>
  <div class="plan-price">$24.95</div>
  <ul class="features">
    <li><svg><use href="#tick-dark"/></svg>Personal Check Up Questionnaire</li>
    <li><svg><use href="#tick-dark"/></svg>E-Mail Questions</li>
    <li><svg><use href="#tick-dark"/></svg>Use of Coaching Tools</li>
    <li><svg><use href="#tick-dark"/></svg>SMS Communication</li>
    <li><svg><use href="#tick-dark"/></svg>Online 30 minute Call/ Meeting - One per Month</li>
    <li><svg><use href="#tick-dark"/></svg>Financial Coaching Annually</li>
  </ul>
  <div class="btn-plan">CHOOSE PLAN</div>
</article>

<article class="plan" style="left:744px">
  <div class="plan-name">Gold</div>
  <div class="plan-price">$149.95</div>
  <ul class="features">
    <li><svg><use href="#tick-muted"/></svg>Personal Check Up Questionnaire</li>
    <li><svg><use href="#tick-muted"/></svg>E-Mail Questions</li>
    <li><svg><use href="#tick-muted"/></svg>Use of Coaching Tools</li>
    <li><svg><use href="#tick-muted"/></svg>SMS Communication</li>
    <li><svg><use href="#tick-muted"/></svg>Online 30 minute Call/ Meeting - One per Week</li>
    <li><svg><use href="#tick-muted"/></svg>Financial Coaching Quarterly</li>
  </ul>
  <div class="btn-plan">CHOOSE PLAN</div>
</article>

<footer class="site-footer">
  <div class="footer-brand">hop3PeakTrail</div>
  <div class="footer-head" style="left:332px">MAIN MENU</div>
  <ul class="footer-menu">
    <li>Who We Are</li>
    <li>Our Model</li>
    <li>Who Uses Hop3peaktrail</li>
    <li>Pricing</li>
  </ul>
  <div class="footer-head" style="left:531px">NEWSLETTER</div>
  <div class="email-field">Enter Email</div>
  <div class="btn-submit">SUBMIT</div>
  <div class="footer-head" style="left:793px">CONTACT US</div>
  <svg class="social" width="145" height="32" viewBox="0 0 145 32" aria-label="Social links">
    <circle cx="15" cy="15" r="14.5" fill="#fff"/>
    <circle cx="52" cy="15" r="14.5" fill="#fff"/>
    <circle cx="89" cy="15" r="14.5" fill="#fff"/>
    <circle cx="125" cy="15" r="14.5" fill="#fff"/>
  </svg>
  <div class="footer-rule"></div>
  <div class="copyright">© 2021 hop3peaktrail. All Rights Reserved.</div>
</footer>
</body>
</html>
```